Professional Single Page Website Design for Velloway Advisory

Velloway Advisory is a new business consultancy specializing in providing expert services to small businesses, primarily in the brick-and-mortar retail and food service sectors. We offer a range of services including franchise development and launch, due diligence, and construction management.

Currently, we have a basic website set up at www.vellowayadvisory.example, but we need a professional touch to enhance its design and functionality.

Project Requirements:
- Single Page Design: For now, we need a single page design that effectively showcases who we are, our services, and contact information.
- Future Expansion: The design should be flexible and scalable for future expansion to include additional pages like specific service offerings, about us, and a dedicated contact page.
- Design Aesthetic: We are looking for a modern yet professional design that aligns with our brand identity.
- Logo: We have a logo that we like, which was also sourced from Pixel Forum. The logo files are attached to this project brief.

Key Sections to Include:
- Hero Section: An engaging introduction to Velloway Advisory with a strong visual impact.
- About Us: A brief overview of who we are and our mission.
- Team: Section for the profiles of the two principals.
- Services: A clear and concise presentation of our services, including franchise development, due diligence, and construction management.
- Contact Information: Easy-to-find contact details, including a form for inquiries.
- Call to Action: Encouraging visitors to get in touch with us for consultations or further information.

Design Considerations:
- Ensure the design is responsive and mobile-friendly.
- Include high-quality images and icons that complement our services and industry.
- We do not need development services, this is only a design project.

```html
<!DOCTYPE html>
<html lang="en">
<head>
<meta charset="utf-8">
<title>Velloway Advisory</title>
<link href="https://fonts.googleapis.com/css2?family=Poppins:wght@300;400;500;600;700&display=swap" rel="stylesheet">
<style>
:root{
  --ink:#1f2a35;
  --ink-deep:#18222b;
  --mint:#9fcfb9;
  --mint-text:#86c4a8;
  --grey-band:#f4f4f4;
  --text:#2b2b2b;
  --muted:#555;
  --white:#fff;
  --line:#e3e3e3;
}
*{box-sizing:border-box;margin:0;padding:0}
html,body{width:1200px;height:4959px;overflow:hidden;background:var(--white)}
body{font-family:'Poppins',sans-serif;color:var(--text)}
.page{position:relative;width:1200px;height:4959px;overflow:hidden}
.abs{position:absolute}

/* header */
.brand{left:77px;top:20px;display:flex;align-items:center;gap:14px}
.brand-dot{width:74px;height:74px;border-radius:50%;background:var(--mint)}
.brand-name{font-weight:600;font-size:23px;line-height:1.05;color:var(--ink)}
.brand-name span{display:block;color:var(--mint-text);font-weight:400}
.nav{top:50px;left:0;width:1200px;font-size:14px;font-weight:500;color:var(--ink)}
.nav a{position:absolute;text-decoration:none;color:inherit;letter-spacing:.3px}
.nav a.active{color:var(--mint-text)}
.nav-underline{left:604px;top:78px;width:56px;height:2px;background:var(--mint)}
.nav-underline::before{content:"";position:absolute;left:-4px;top:-3px;width:8px;height:8px;border-radius:50%;background:var(--mint)}

/* hero */
.hero{top:118px;left:0;width:1200px;height:778px}
.hero-photo{left:0;top:0;width:603px;height:778px;background:linear-gradient(160deg,#8d969c 0%,#5f6a66 35%,#3d4a3f 70%,#2d3a30 100%)}
.hero-panel{left:603px;top:0;width:597px;height:778px;background:#2c3844}
.hero-copy{right:58px;top:185px;text-align:right;color:var(--white)}
.hero-title{font-weight:600;font-size:58px;line-height:1}
.hero-sub{font-weight:400;font-size:44px;line-height:1.15;margin-top:4px}
.hero-sub em{font-style:normal;color:var(--mint)}
.hero-tag{font-weight:300;font-size:37px;line-height:1.2;margin-top:30px}
.btn-mint{display:inline-block;background:var(--mint);color:var(--white);font-weight:500;font-size:16px;border-radius:30px;width:188px;height:57px;line-height:57px;text-align:center;margin-top:40px}
.hero-edge{left:0;bottom:0}

/* headings */
.sec-head{display:flex;align-items:center;gap:14px}
.sec-dot{width:96px;height:96px;border-radius:50%;background:var(--mint)}
.sec-title{font-weight:600;font-size:46px;line-height:1;color:var(--ink)}
.sec-title span{display:block;font-weight:400;font-size:32px;color:var(--mint-text);margin-top:2px}
.sec-head.small .sec-dot{width:78px;height:78px}
.sec-head.small .sec-title{font-size:40px}
.sec-head.small .sec-title span{font-size:24px}

/* diamonds */
.diamond{position:absolute;transform:translate(-50%,-50%) rotate(45deg);border-radius:26%}

/* about */
.about-copy{left:644px;top:1105px;width:424px;font-size:13.5px;line-height:27px;color:var(--muted);text-align:justify;font-weight:300}
.btn-dark{display:block;background:var(--ink);color:var(--white);font-weight:500;font-size:12px;border-radius:26px;text-align:center}
.about-btn{left:645px;top:1381px;width:162px;height:50px;line-height:50px}

/* services */
.service{width:340px;text-align:center}
.service h3{font-weight:600;font-size:23px;color:var(--ink)}
.service p{font-size:13px;line-height:22px;color:var(--muted);font-weight:300;width:270px;margin:8px auto 0}

/* team */
.team-card{top:2585px;width:314px;height:418px;text-align:center}
.team-card.light{background:var(--white);box-shadow:0 2px 12px rgba(0,0,0,.12)}
.team-card.mint{background:#a9d6c2}
.team-card h4{position:absolute;left:0;width:100%;top:256px;font-weight:600;font-size:22px;color:var(--ink)}
.team-card .role{position:absolute;left:0;width:100%;top:287px;font-size:17px;color:var(--mint-text)}
.team-card.mint .role{color:var(--white)}
.team-card .icons{position:absolute;left:0;width:100%;top:329px;display:flex;justify-content:center;gap:18px}
.icon-circle{width:46px;height:46px;border-radius:50%;display:flex;align-items:center;justify-content:center}
.team-card.light .icon-circle{background:var(--ink)}
.team-card.mint .icon-circle{background:var(--white)}

/* contact */
.contact-lead{left:0;top:3450px;width:1200px;text-align:center;font-size:23px;color:var(--ink)}
.contact-box{left:75px;top:3553px;width:1050px;height:813px;background:var(--grey-band)}
.info{left:143px;display:flex;align-items:center;gap:18px}
.info-icon{width:74px;height:74px;border-radius:50%;display:flex;align-items:center;justify-content:center}
.info-icon.dark{background:var(--ink)}
.info-icon.mint{background:var(--mint)}
.info h5{font-weight:500;font-size:20px;color:var(--ink)}
.info p{font-size:13px;color:var(--ink);margin-top:2px}
.form-card{left:470px;top:3623px;width:609px;height:670px;background:var(--white)}
.f-label{position:absolute;left:71px;font-size:13px;font-weight:500;color:var(--ink)}
.f-field{position:absolute;border:1px solid var(--line);font-size:12px;color:#aaa;padding:0 20px;display:flex;align-items:center;font-weight:300}
.f-field.area{align-items:flex-start;padding-top:14px}
.submit{left:218px;top:566px;width:175px;height:52px;line-height:52px;font-size:16px;border-radius:30px}

/* footer */
.footer{left:0;top:4449px;width:1200px;height:510px}
.foot-col h6{font-weight:500;font-size:21px;color:var(--white)}
.foot-rule{position:absolute;height:2px;background:var(--mint)}
.foot-rule::after{content:"";position:absolute;right:-4px;top:-3px;width:8px;height:8px;border-radius:50%;background:var(--mint)}
.foot-links{list-style:none;margin-top:36px}
.foot-links li{font-size:13px;color:var(--white);height:26px;display:flex;align-items:center;gap:8px;font-weight:300}
.foot-links li::before{content:"";width:9px;height:9px;border:2px solid var(--mint);transform:rotate(45deg)}
.foot-brand{left:0;width:1200px;text-align:center;top:4618px}
.foot-brand .brand-dot{width:80px;height:80px;margin:0 auto}
.foot-brand p{font-weight:500;font-size:20px;color:var(--white);margin-top:14px}
.socials{display:flex;justify-content:center;gap:16px;margin-top:20px}
.socials span{width:30px;height:30px;border:2px solid var(--white);transform:rotate(45deg);border-radius:4px}
.foot-contact{display:flex;align-items:center;gap:14px;font-size:12.5px;color:var(--white);line-height:16px;font-weight:300;height:50px}
.foot-contact i{width:26px;height:26px;border:2px solid var(--white);transform:rotate(45deg);flex:none;margin-left:6px}
.copyright{left:0;top:4902px;width:1200px;height:57px;background:var(--ink-deep);color:var(--white);font-size:12px;text-align:center;line-height:57px;font-weight:300}
</style>
</head>
<body>
<div class="page">

  <!-- header -->
  <div class="abs brand"><div class="brand-dot"></div><div class="brand-name">Velloway<span>Advisory</span></div></div>
  <nav class="abs nav">
    <a class="active" style="left:612px">HOME</a>
    <a style="left:691px">WHO WE ARE</a>
    <a style="left:822px">OUR SERVICES</a>
    <a style="left:961px">TEAM</a>
    <a style="left:1031px">CONTACT US</a>
  </nav>
  <div class="abs nav-underline"></div>

  <!-- hero -->
  <section class="abs hero">
    <div class="abs hero-photo" role="img" aria-label="Modern multi-storey apartment building with balconies and evergreen trees"></div>
    <div class="abs hero-panel"></div>
    <div class="abs hero-copy">
      <h1 class="hero-title">Building Success</h1>
      <p class="hero-sub">in <em>Southern California</em></p>
      <p class="hero-tag">Expertise at Every Step:<br>From Planning to Execution</p>
      <a class="btn-mint">LEARN MORE</a>
    </div>
    <svg class="abs hero-edge" width="1200" height="180" viewBox="0 0 1200 180">
      <polygon points="0,0 603,160 1200,0 1200,60 603,178 0,60" fill="#9fcfb9"/>
      <polygon points="0,60 603,178 1200,60 1200,180 0,180" fill="#fff"/>
    </svg>
  </section>

  <!-- about -->
  <div class="diamond" style="left:340px;top:1212px;width:290px;height:290px;background:linear-gradient(135deg,#d7dcdf,#6f7a7a 60%,#3d4744)" role="img" aria-label="Apartment building photograph framed in a rounded diamond"></div>
  <div class="abs sec-head small" style="left:636px;top:995px"><div class="sec-dot"></div><h2 class="sec-title">About Us<span>Who We Are</span></h2></div>
  <p class="abs about-copy">Welcome to Velloway Advisory, your trusted partner in navigating the complexities of the real estate and small business markets. Founded by industry veterans Rafael Dunmore and Kevin Ashcroft, we specialize in providing comprehensive services tailored to the unique needs of our clients. Whether you're a franchisee, a new restaurant owner, or a commercial real estate investor, our expertise in due diligence, construction management, and investment property evaluation ensures you make informed, strategic decisions.</p>
  <a class="abs btn-dark about-btn">READ MORE</a>

  <!-- services -->
  <div class="abs sec-head" style="left:388px;top:1563px"><div class="sec-dot" style="width:102px;height:102px"></div><h2 class="sec-title">Our Services<span>What We Do</span></h2></div>
  <div class="diamond" style="left:227px;top:1888px;width:226px;height:226px;background:linear-gradient(135deg,#2f3a44,#b98b5a 60%,#d9b88a)" role="img" aria-label="Hands stacking wooden blocks"></div>
  <div class="diamond" style="left:607px;top:1888px;width:226px;height:226px;background:linear-gradient(135deg,#3a4a5a,#c9b48e 45%,#eef1f2)" role="img" aria-label="Business people reviewing charts on paper"></div>
  <div class="diamond" style="left:975px;top:1888px;width:226px;height:226px;background:linear-gradient(135deg,#5c7ea8,#dfe5ea 50%,#3f5f86)" role="img" aria-label="Construction team reviewing blueprints around a table"></div>
  <div class="abs service" style="left:57px;top:2060px"><h3>Franchise Development</h3><p>Comprehensive franchise setup from evaluation to launch for scalable business growth.</p></div>
  <div class="abs service" style="left:437px;top:2060px"><h3>Due Diligence</h3><p>Comprehensive franchise setup from evaluation to launch for scalable business growth.</p></div>
  <div class="abs service" style="left:805px;top:2060px"><h3>Construction Management</h3><p>Comprehensive franchise setup from evaluation to launch for scalable business growth.</p></div>

  <!-- team -->
  <svg class="abs" style="left:0;top:2273px" width="1200" height="934" viewBox="0 0 1200 934">
    <polygon points="0,163 600,0 1200,163 1200,770 600,934 0,770" fill="#f4f4f4"/>
  </svg>
  <div class="abs sec-head" style="left:421px;top:2413px"><div class="sec-dot" style="width:104px;height:104px"></div><h2 class="sec-title">Our Team<span>Velloway</span></h2></div>
  <div class="abs team-card light" style="left:266px">
    <div class="diamond" style="left:157px;top:133px;width:152px;height:152px;background:linear-gradient(135deg,#9fb6c9,#c9a68a 55%,#e6e9ef)" role="img" aria-label="Portrait of principal Rafael Dunmore"></div>
    <h4>Rafael Dunmore</h4><p class="role">Principal</p>
    <div class="icons">
      <span class="icon-circle"><svg width="20" height="20" viewBox="0 0 24 24"><path d="M6.6 10.8a15 15 0 0 0 6.6 6.6l2.2-2.2a1 1 0 0 1 1-.25 11 11 0 0 0 3.6.6 1 1 0 0 1 1 1V20a1 1 0 0 1-1 1A17 17 0 0 1 3 4a1 1 0 0 1 1-1h3.5a1 1 0 0 1 1 1 11 11 0 0 0 .6 3.6 1 1 0 0 1-.25 1z" fill="#fff"/></svg></span>
      <span class="icon-circle"><svg width="20" height="16" viewBox="0 0 20 16"><rect x="1" y="1" width="18" height="14" rx="1" fill="#fff"/><path d="M1 1l9 7 9-7" stroke="#1f2a35" stroke-width="1.5" fill="none"/></svg></span>
    </div>
  </div>
  <div class="abs team-card mint" style="left:620px">
    <div class="diamond" style="left:157px;top:133px;width:152px;height:152px;background:linear-gradient(135deg,#8a7d6c,#6b4f3c 55%,#2c2a2a)" role="img" aria-label="Portrait of principal Kevin Ashcroft"></div>
    <h4>Kevin Ashcroft</h4><p class="role">Principal</p>
    <div class="icons">
      <span class="icon-circle"><svg width="20" height="20" viewBox="0 0 24 24"><path d="M6.6 10.8a15 15 0 0 0 6.6 6.6l2.2-2.2a1 1 0 0 1 1-.25 11 11 0 0 0 3.6.6 1 1 0 0 1 1 1V20a1 1 0 0 1-1 1A17 17 0 0 1 3 4a1 1 0 0 1 1-1h3.5a1 1 0 0 1 1 1 11 11 0 0 0 .6 3.6 1 1 0 0 1-.25 1z" fill="#1f2a35"/></svg></span>
      <span class="icon-circle"><svg width="20" height="16" viewBox="0 0 20 16"><rect x="1" y="1" width="18" height="14" rx="1" fill="#1f2a35"/><path d="M1 1l9 7 9-7" stroke="#fff" stroke-width="1.5" fill="none"/></svg></span>
    </div>
  </div>

  <!-- contact -->
  <div class="abs sec-head" style="left:391px;top:3322px"><div class="sec-dot" style="width:104px;height:104px"></div><h2 class="sec-title">Contact Us<span>Get In Touch</span></h2></div>
  <p class="abs contact-lead">Encouraging visitors to get in touch with us for consultations or further information.</p>
  <div class="abs contact-box"></div>
  <div class="abs info" style="top:3749px">
    <div class="info-icon dark"><svg width="26" height="34" viewBox="0 0 26 34"><path d="M13 1C6.4 1 1 6.2 1 12.6 1 21.6 13 33 13 33s12-11.4 12-20.4C25 6.2 19.6 1 13 1z" fill="#fff"/><circle cx="13" cy="12.5" r="4.5" fill="#1f2a35"/></svg></div>
    <div><h5>LOCATION</h5><p>Address line dummy Here</p></div>
  </div>
  <div class="abs info" style="top:3933px">
    <div class="info-icon mint"><svg width="32" height="32" viewBox="0 0 24 24"><path d="M6.6 10.8a15 15 0 0 0 6.6 6.6l2.2-2.2a1 1 0 0 1 1-.25 11 11 0 0 0 3.6.6 1 1 0 0 1 1 1V20a1 1 0 0 1-1 1A17 17 0 0 1 3 4a1 1 0 0 1 1-1h3.5a1 1 0 0 1 1 1 11 11 0 0 0 .6 3.6 1 1 0 0 1-.25 1z" fill="none" stroke="#fff" stroke-width="1.6"/></svg></div>
    <div><h5>CALL US</h5><p>8000 555 0134</p></div>
  </div>
  <div class="abs info" style="top:4125px">
    <div class="info-icon dark"><svg width="34" height="26" viewBox="0 0 20 16"><rect x="1" y="1" width="18" height="14" rx="1" fill="none" stroke="#fff" stroke-width="1.4"/><path d="M1 1l9 7 9-7M1 15l7-6M19 15l-7-6" stroke="#fff" stroke-width="1.4" fill="none"/></svg></div>
    <div><h5>EMAIL US</h5><p>info@vellowayadvisory.example</p></div>
  </div>
  <form class="abs form-card">
    <label class="f-label" style="top:42px">TELL US YOUR NAME *</label>
    <div class="f-field" style="left:71px;top:69px;width:224px;height:46px">First Name:</div>
    <div class="f-field" style="left:314px;top:69px;width:224px;height:46px">Last Name:</div>
    <label class="f-label" style="top:146px">ENTER YOUR EMAIL *</label>
    <div class="f-field" style="left:71px;top:173px;width:467px;height:46px">Email:</div>
    <label class="f-label" style="top:249px">ENTER PHONE NUMBER</label>
    <div class="f-field" style="left:71px;top:275px;width:467px;height:46px">Phone:</div>
    <label class="f-label" style="top:353px">MESSAGE *</label>
    <div class="f-field area" style="left:71px;top:379px;width:467px;height:153px">Write us a message</div>
    <a class="abs btn-dark submit">SUBMIT NOW</a>
  </form>

  <!-- footer -->
  <footer class="abs footer">
    <svg class="abs" style="left:0;top:0" width="1200" height="510" viewBox="0 0 1200 510">
      <polygon points="0,115 600,0 1200,115 1200,175 600,16 0,175" fill="#9fcfb9"/>
      <polygon points="0,175 600,16 1200,175 1200,510 0,510" fill="#1f2a35"/>
    </svg>
  </footer>
  <div class="abs foot-col" style="left:233px;top:4648px">
    <h6>Quik Links</h6>
    <ul class="foot-links">
      <li>Home</li><li>Who We Are</li><li>Our Services</li><li>Team</li><li>Contact Us</li>
    </ul>
  </div>
  <div class="abs foot-rule" style="left:233px;top:4688px;width:150px"></div>
  <div class="abs foot-brand">
    <div class="brand-dot"></div>
    <p>Velloway Advisory</p>
    <div class="socials"><span></span><span></span><span></span><span></span></div>
  </div>
  <div class="abs foot-col" style="left:790px;top:4648px">
    <h6>Contact Details</h6>
    <div style="margin-top:30px">
      <div class="foot-contact"><i></i><span>CALL US<br>8000 555 0134</span></div>
      <div class="foot-contact"><i></i><span>EMAIL US<br>info@vellowayadvisory.example</span></div>
      <div class="foot-contact"><i></i><span>Address line here dummy<br>Address line here</span></div>
    </div>
  </div>
  <div class="abs foot-rule" style="left:790px;top:4688px;width:215px"></div>
  <div class="abs copyright">Copyright © 2024 All Rights Reserved By Company name</div>

</div>
</body>
</html>
```